Cosmetic injections clinic needs a fresh looking business card

We need a business card using the supplied logo and color scheme to attract future clients to our clinic. It should be modern and fresh, eye catching and not too busy. Simple and to the point is best. I would like two sided designs with the front indicating address and contact information, and the back in full color with white logo and descriptive information also provided.
Target Market(s)
Clients looking for non surgical beauty enhancements.
Contact Information for Business Card
MeloraSkin
14, 618 Birchmont Way
St. Albert, Alberta
K2P 7W3
Phone: 587-412-6630
Email: info@meloraskin.com
Requirements
Must have
- -Logo supplied with the name and address of the clinic
- -Back of card in full color with white logo with A small line of text indicating both of the following: Anti aging consultants and cosmetic injectables
- Located inside the Voyager Wellness Group

```html
<!DOCTYPE html>
<html lang="en">
<head>
<meta charset="utf-8">
<title>MeloraSkin — Business Card Back</title>
<link rel="stylesheet" href="https://fonts.googleapis.com/css2?family=Arimo:wght@700&display=swap">
<style>
  :root {
    --page: #ffffff;
    --magenta-deep: #c1228a;
    --magenta-mid: #d62f93;
    --magenta-bright: #e6399c;
    --magenta-soft: #d9449e;
    --ink-light: #ffffff;
  }
  html, body {
    margin: 0;
    padding: 0;
    width: 1200px;
    height: 777px;
    overflow: hidden;
    background: var(--page);
  }
  .card-back {
    position: relative;
    width: 1200px;
    height: 777px;
    border-radius: 16px;
    overflow: hidden;
  }
  .card-back__pattern {
    position: absolute;
    inset: 0;
    background:
      radial-gradient(ellipse at 75% 85%, var(--magenta-bright) 0%, transparent 55%),
      radial-gradient(ellipse at 20% 15%, var(--magenta-deep) 0%, transparent 60%),
      linear-gradient(160deg, var(--magenta-soft) 0%, var(--magenta-mid) 50%, var(--magenta-bright) 100%);
  }
  .brand {
    position: absolute;
    left: 365px;
    top: 285px;
    height: 150px;
    display: flex;
    align-items: center;
    gap: 26px;
  }
  .brand__mark {
    width: 150px;
    height: 150px;
    border-radius: 50%;
    background: var(--ink-light);
    flex: none;
  }
  .brand__name {
    font-family: "Arimo", Arial, sans-serif;
    font-weight: 700;
    font-size: 60px;
    color: var(--ink-light);
    line-height: 1;
  }
  .tagline {
    position: absolute;
    left: 0;
    right: 0;
    top: 486px;
    margin: 0;
    text-align: center;
    font-family: "Arimo", Arial, sans-serif;
    font-weight: 700;
    font-size: 30px;
    color: var(--ink-light);
    line-height: 1.2;
  }
</style>
</head>
<body>
  <main class="card-back">
    <div class="card-back__pattern" role="img" aria-label="Magenta low-poly faceted triangle background pattern"></div>
    <div class="brand">
      <span class="brand__mark" aria-hidden="true"></span>
      <span class="brand__name">MeloraSkin</span>
    </div>
    <p class="tagline">Anti aging consultants and cosmetic injectables</p>
  </main>
</body>
</html>
```